NEW Modern Sleek Business Card for VR Language Startup

Our startup is using VR to lead the next wave of world language education. We need a two-sided business card that introduces the larger organization (Quorvel Language Inc) and our contact info on one side and shows the product, Lumidrasca, on the other side.

Side 1 (contact info)= Quorvel Logo and Contact info (name, title, phone, email)

Side 2 (product)= Lumidrasc logo, text, and website
Text= Culturally Immersive Language Learning Games
Website= www.lumidrasc.example

Target Market(s)

Education, Technology

Contact Information for Business Card

Contact info will be updated upon approval of the design. For now, put this as a placeholder.

Perry Hollins
Founder & CEO
phollins@mailtrove.example
(555)-014-2736

Font styles to use
Other font styles liked:
• Gibson and Century Gothic are the brand fonts

Requirements
Nice to have
• I would love to see cohesion between the design and colors of the two logos. I have attached a few business card designs that I like, so you can get a feel for my preferred style.

```html
<!DOCTYPE html>
<html lang="en">
<head>
<meta charset="utf-8">
<title>Quorvel Language Inc – Business Card</title>
<link href="https://fonts.googleapis.com/css2?family=Montserrat:wght@500;600;700;800&family=Questrial&display=swap" rel="stylesheet">
<style>
  :root {
    --stage: #2a2b2e;
    --ink: #050505;
    --paper: #ffffff;
    --violet: #7b4dff;
    --magenta: #e6338f;
    --coral: #ff5a3c;
    --amber: #ffc83a;
    --cyan: #35c8f0;
    --text-light: #f4f4f4;
    --text-soft: #cfcfd4;
  }
  * { box-sizing: border-box; margin: 0; padding: 0; }
  html, body {
    width: 1200px; height: 900px; overflow: hidden;
    background: var(--stage);
  }
  .stage { position: relative; width: 1200px; height: 900px; }

  .card {
    position: absolute;
    border-radius: 22px;
    overflow: hidden;
    box-shadow: 0 18px 40px rgba(0,0,0,.55);
  }
  .card svg.card-art { position: absolute; inset: 0; display: block; }

  .brand {
    display: flex; align-items: center; gap: 12px;
    font-family: "Montserrat", sans-serif;
    font-weight: 800; letter-spacing: 4px; line-height: 1;
  }
  .brand__dot {
    flex: none;
    width: 30px; height: 30px; border-radius: 50%;
    background: var(--magenta);
  }

  /* Contact side (portrait) */
  .card--contact { left: 150px; top: 152px; width: 340px; height: 595px; }
  .card--contact .brand {
    position: absolute; left: 0; right: 0; top: 100px;
    justify-content: center; font-size: 32px; color: var(--ink);
  }

  .person { position: absolute; left: 44px; top: 360px; }
  .person__name {
    font-family: "Montserrat", sans-serif; font-weight: 800;
    font-size: 30px; line-height: 1;
    background: linear-gradient(90deg, var(--amber), var(--coral), var(--magenta), var(--violet), var(--cyan));
    -webkit-background-clip: text; background-clip: text; color: transparent;
  }
  .person__title {
    margin-top: 6px;
    font-family: "Questrial", sans-serif; font-size: 17px; color: var(--text-light);
  }
  .contacts {
    position: absolute; left: 0; right: 0; top: 452px;
    display: flex; flex-direction: column; align-items: center; gap: 10px;
    font-family: "Questrial", sans-serif; font-size: 14px; color: var(--text-light);
  }
  .contacts__item { display: flex; flex-direction: column; align-items: center; gap: 5px; }
  .contacts__icon { width: 26px; height: 26px; }

  /* Product side (landscape) */
  .card--product { left: 548px; top: 280px; width: 595px; height: 340px; }
  .product {
    position: absolute; left: 0; right: 0; top: 112px;
    display: flex; flex-direction: column; align-items: center; gap: 16px;
    text-align: center;
  }
  .product .brand { font-size: 34px; color: var(--paper); }
  .product__tagline {
    font-family: "Questrial", sans-serif; font-size: 15px;
    letter-spacing: 1px; color: var(--text-soft);
  }
  .product__web {
    margin-top: 14px;
    font-family: "Questrial", sans-serif; font-size: 15px;
    letter-spacing: 1px; color: var(--text-light);
  }
</style>
</head>
<body>
<main class="stage">
  <svg width="0" height="0" aria-hidden="true" style="position:absolute">
    <defs>
      <linearGradient id="spectrum" x1="0" y1="1" x2="1" y2="0">
        <stop offset="0" stop-color="#7b4dff"/>
        <stop offset=".4" stop-color="#e6338f"/>
        <stop offset=".75" stop-color="#ff5a3c"/>
        <stop offset="1" stop-color="#ffc83a"/>
      </linearGradient>
    </defs>
  </svg>

  <section class="card card--contact" aria-label="Contact side">
    <svg class="card-art" viewBox="0 0 340 595" aria-hidden="true">
      <rect width="340" height="595" fill="url(#spectrum)"/>
      <path d="M0,0 H340 V140 C340,235 230,270 140,310 C70,342 25,372 0,400 Z" fill="var(--paper)"/>
      <path d="M0,432 C40,392 90,362 150,334 C250,290 330,262 340,172 V430 C340,482 300,505 250,532 C195,562 170,578 152,595 H0 Z" fill="var(--ink)"/>
    </svg>
    <div class="brand"><span class="brand__dot"></span><span>QUORVEL</span></div>
    <div class="person">
      <p class="person__name">Perry Hollins</p>
      <p class="person__title">Founder &amp; CEO</p>
    </div>
    <div class="contacts">
      <div class="contacts__item">
        <svg class="contacts__icon" viewBox="0 0 26 26" aria-hidden="true">
          <circle cx="13" cy="13" r="13" fill="var(--paper)"/>
          <rect x="6.5" y="8.5" width="13" height="9" rx="1" fill="none" stroke="var(--ink)" stroke-width="1.6"/>
          <path d="M6.5,9 L13,14 L19.5,9" fill="none" stroke="var(--ink)" stroke-width="1.6"/>
        </svg>
        <span>phollins@mailtrove.example</span>
      </div>
      <div class="contacts__item">
        <svg class="contacts__icon" viewBox="0 0 26 26" aria-hidden="true">
          <circle cx="13" cy="13" r="13" fill="var(--paper)"/>
          <path d="M9.5,6.5 C8,7.5 7.5,9.5 8.5,12 C10,15.5 12.5,18 15.5,19.3 C17.5,20 19,19.2 19.6,18 L17.3,15.6 L15.2,16.6 C13.4,15.6 11.4,13.6 10.5,11.8 L11.6,9.8 Z" fill="var(--ink)"/>
        </svg>
        <span>(555)-014-2736</span>
      </div>
    </div>
  </section>

  <section class="card card--product" aria-label="Product side">
    <svg class="card-art" viewBox="0 0 595 340" aria-hidden="true">
      <rect width="595" height="340" fill="url(#spectrum)"/>
      <path d="M95,0 H532 C562,40 560,92 522,152 C474,230 470,298 502,340 H58 C88,300 94,258 60,200 C32,150 42,60 95,0 Z" fill="var(--ink)"/>
    </svg>
    <div class="product">
      <div class="brand"><span class="brand__dot"></span><span>LUMIDRASC</span></div>
      <p class="product__tagline">Culturally Immersive Language Learning Games</p>
      <p class="product__web">www.lumidrasc.example</p>
    </div>
  </section>
</main>
</body>
</html>
```